Letterhead Creation

I would like to create a letterhead incorporating my family crest attached. My current letterhead with my information is also attached. I would also like to add my Paralegal Rosalind Merriweather

```html
<!DOCTYPE html>
<html lang="en">
<head>
<meta charset="utf-8">
<title>Law Offices of Daniel R. Holloway – Letterhead</title>
<link rel="stylesheet" href="https://fonts.googleapis.com/css2?family=Bebas+Neue&family=PT+Sans:wght@400&display=swap">
<style>
  :root {
    --paper: #ffffff;
    --ink: #6a6a6a;
    --title: #666666;
    --rule: #3a3a3a;
    --crest-blue: #2c4a9a;
    --crest-grey: #b9bcc4;
    --icon: #6f6f6f;
  }
  * { margin: 0; padding: 0; box-sizing: border-box; }
  html, body { width: 992px; height: 1200px; overflow: hidden; background: var(--paper); }
  .letterhead {
    position: relative; width: 992px; height: 1200px; background: var(--paper);
    font-family: "PT Sans", "Myriad Pro", sans-serif; color: var(--ink);
  }
  .crest {
    position: absolute; left: 225px; top: 73px; width: 160px; height: 158px;
    border-radius: 40% 40% 48% 48%;
    background: radial-gradient(circle at 50% 60%, var(--crest-blue) 0 45%, var(--crest-grey) 75%, #e4e6ea 100%);
  }
  .firm-name {
    position: absolute; left: 415px; top: 108px; width: 350px; text-align: center;
    font-family: "Bebas Neue", sans-serif; font-weight: 400; font-size: 44px; line-height: 48px;
    color: var(--title); white-space: nowrap;
  }
  .paralegal {
    position: absolute; left: 415px; top: 214px; width: 350px; text-align: center;
    font-size: 14px; line-height: 18px; color: var(--ink); white-space: nowrap;
  }
  .rule { position: absolute; height: 1.5px; background: var(--rule); }
  .rule--top { left: 86px; width: 810px; top: 254px; }
  .rule--bottom { left: 91px; width: 810px; top: 1084px; }
  .letter-body {
    position: absolute; left: 103px; top: 327px; width: 802px;
    font-size: 17.4px; line-height: 21px; text-align: justify; color: var(--ink);
  }
  .letter-body p + p { margin-top: 21px; }
  .signature-mark {
    position: absolute; left: 700px; top: 972px; width: 165px; height: 34px;
    background: linear-gradient(90deg, #eeeeee, #dedede, #eeeeee); border-radius: 4px;
  }
  .signer { position: absolute; left: 700px; top: 1010px; width: 165px; text-align: center; font-size: 16px; }
  .address { position: absolute; left: 0; width: 992px; top: 1100px; text-align: center; font-size: 14.5px; }
  .contacts {
    position: absolute; left: 0; width: 992px; top: 1126px;
    display: flex; justify-content: center; gap: 16px; font-size: 14.5px;
  }
  .contact { display: flex; align-items: center; gap: 9px; }
  .contact svg { width: 14px; height: 14px; fill: var(--icon); }
</style>
</head>
<body>
<main class="letterhead">
  <div class="crest" role="img" aria-label="Family crest: blue shield with helmet and scrolled mantling"></div>
  <h1 class="firm-name">Law Offices of<br>Daniel R. Holloway</h1>
  <p class="paralegal">Paralegal: Rosalind Merriweather</p>
  <div class="rule rule--top"></div>

  <section class="letter-body">
    <p>Lorem ipsum dolor sit amet, consectetur adipiscing elit, sed do eiusmod tempor incididunt ut labore et dolore magna aliqua. Ut enim ad minim veniam, quis nostrud exercitation ullamco laboris nisi ut aliquip ex ea commodo consequat. Duis aute irure dolor in reprehenderit in voluptate velit esse cillum dolore eu fugiat nulla pariatur. Excepteur sint occaecat cupidatat non proident, sunt in culpa qui officia deserunt mollit anim id est laborum</p>
    <p>Sed ut perspiciatis unde omnis iste natus error sit voluptatem accusantium doloremque laudantium, totam rem aperiam, eaque ipsa quae ab illo inventore veritatis et quasi architecto beatae vitae dicta sunt explicabo. Nemo enim ipsam voluptatem quia voluptas sit aspernatur aut odit aut fugit, sed quia consequuntur magni dolores eos qui ratione voluptatem sequi nesciunt. Neque porro quisquam est, qui dolorem ipsum quia dolor sit amet, consectetur, adipisci velit, sed quia non numquam eius modi tempora incidunt ut labore et dolore magnam aliquam quaerat voluptatem. Ut enim ad minima veniam, quis nostrum exercitationem ullam corporis suscipit laboriosam, nisi ut aliquid ex ea commodi consequatur? Quis autem vel eum iure reprehenderit qui in ea voluptate velit esse quam nihil molestiae consequatur, vel illum qui dolorem eum fugiat quo voluptas nulla pariatur?</p>
    <p>Lorem ipsum dolor sit amet, consectetur adipiscing elit, sed do eiusmod tempor incididunt ut labore et dolore magna aliqua. Ut enim ad minim veniam, quis nostrud exercitation ullamco laboris nisi ut aliquip ex ea commodo consequat. Duis aute irure dolor in reprehenderit in voluptate velit esse cillum dolore eu fugiat nulla pariatur. Excepteur sint occaecat cupidatat non proident, sunt in culpa qui officia deserunt mollit anim id est laborum</p>
    <p>Sed ut perspiciatis unde omnis iste natus error sit voluptatem accusantium doloremque laudantium, totam rem aperiam, eaque ipsa quae ab illo inventore veritatis et quasi architecto beatae vitae dicta sunt explicabo. Nemo enim ipsam voluptatem quia voluptas sit aspernatur aut odit aut fugit, sed quia consequuntur magni dolores eos qui ratione voluptatem sequi nesciunt. Neque porro quisquam est, qui dolorem ipsum quia dolor sit amet, consectetur, adipisci velit, sed quia non numquam eius modi tempora incidunt ut labore et dolore magnam aliquam quaerat voluptatem. Ut enim ad minima veniam, quis</p>
  </section>

  <div class="signature-mark" role="img" aria-label="Handwritten signature"></div>
  <p class="signer">Name Name</p>

  <div class="rule rule--bottom"></div>
  <p class="address">Daniel Holloway Esq, 415 N. Alder Ave, Glendora, Ca 91740</p>
  <div class="contacts">
    <span class="contact">
      <svg viewBox="0 0 16 16" aria-hidden="true"><circle cx="8" cy="8" r="8"/><path d="M5 4.5l1.5-.5 1 2-1 .8a5 5 0 0 0 2.7 2.7l.8-1 2 1-.5 1.5c-3.5.3-6.8-3-6.5-6.5z" fill="#fff"/></svg>
      (555) 201-4837
    </span>
    <span class="contact">
      <svg viewBox="0 0 16 16" aria-hidden="true"><circle cx="8" cy="8" r="8"/><rect x="4" y="6" width="8" height="5" rx="1" fill="#fff"/><rect x="5.5" y="4" width="5" height="2" fill="#fff"/></svg>
      (555) 201-4838
    </span>
    <span class="contact">
      <svg viewBox="0 0 16 16" aria-hidden="true"><circle cx="8" cy="8" r="8"/><rect x="4" y="5" width="8" height="6" rx="0.5" fill="#fff"/><path d="M4 5l4 3.2L12 5" stroke="#6f6f6f" stroke-width="1" fill="none"/></svg>
      Daniel@hollowaylawapc.com
    </span>
    <span class="contact">
      <svg viewBox="0 0 16 16" aria-hidden="true"><circle cx="8" cy="8" r="7" fill="none" stroke="#6f6f6f" stroke-width="1.6"/><ellipse cx="8" cy="8" rx="3" ry="7" fill="none" stroke="#6f6f6f" stroke-width="1.2"/><path d="M1 8h14M2.5 4.5h11M2.5 11.5h11" stroke="#6f6f6f" stroke-width="1.2"/></svg>
      www.hollowaylawapc.com
    </span>
  </div>
</main>
</body>
</html>
```